Redesign of Website

We need an overhaul of our website. I've attached our current logo files. Please visit www.qelvorbis.com for our current website for information about our company. We are looking for the same type of website (information-based only) so no need for any online store, payments, interactive stuff or anything like that...basically looking for a fresh new look! Also please make sure this design will be mobile-friendly. Thanks!

```html
<!DOCTYPE html>
<html lang="en">
<head>
<meta charset="utf-8">
<title>Qelvorbis Consultants</title>
<link href="https://fonts.googleapis.com/css2?family=Montserrat:wght@400;500;600;700&display=swap" rel="stylesheet">
<style>
  :root {
    --navy: #083f86;
    --navy-deep: #062b5e;
    --ink: #111418;
    --body: #333;
    --muted: #9a9a9a;
    --white: #ffffff;
    --line: #d9dde3;
    --sand: #f3ece2;
  }
  * { box-sizing: border-box; margin: 0; padding: 0; }
  html, body { width: 716px; height: 1200px; overflow: hidden; background: var(--white); }
  body { font-family: "Montserrat", Arial, sans-serif; color: var(--ink); position: relative; }
  .abs { position: absolute; }

  /* Hero */
  .hero {
    left: 0; top: 0; width: 716px; height: 330px;
    background: linear-gradient(100deg, #0a3470 0%, #0b3c80 45%, #14457f 70%, #0b3a77 100%);
    border-bottom-left-radius: 42px;
  }
  .site-nav { left: 96px; top: 16px; width: 524px; height: 30px; display: flex; align-items: center; justify-content: space-between; }
  .brand { color: var(--white); font-weight: 700; font-size: 13px; letter-spacing: .5px; display: flex; align-items: center; gap: 5px; }
  .brand-dot { width: 8px; height: 8px; background: var(--white); }
  .nav-links { display: flex; gap: 22px; font-size: 7.5px; font-weight: 500; color: var(--white); }
  .hero-title { left: 96px; top: 128px; width: 420px; font-size: 15.5px; line-height: 24px; font-weight: 500; color: var(--white); }
  .btn { display: flex; align-items: center; justify-content: center; font-size: 7.5px; font-weight: 500; border-radius: 2px; }
  .btn-light { background: var(--white); color: var(--navy-deep); }
  .btn-dark { background: var(--navy); color: var(--white); }

  /* About */
  .house-photo { left: 410px; top: 292px; width: 210px; height: 241px; border-radius: 10px;
    background: linear-gradient(180deg, #9cc1df 0%, #b9b2aa 30%, #d7c9bd 60%, #c5b7aa 100%); }
  .eyebrow { left: 96px; top: 369px; font-size: 6px; letter-spacing: 1px; color: var(--navy); font-weight: 500; }
  .section-title { font-size: 13.5px; font-weight: 500; line-height: 19px; color: var(--ink); }
  .copy { font-size: 7.2px; line-height: 14.5px; color: var(--body); }

  /* Services */
  .services-band { left: 0; top: 583px; width: 716px; height: 148px;
    background: linear-gradient(90deg, #ecebe8 0%, #f1ede7 50%, #f7efe3 80%, #fbf4ea 100%); border-top-left-radius: 30px; }
  .service-card { width: 120px; height: 107px; background: var(--navy); border-radius: 10px;
    color: var(--white); font-size: 7px; font-weight: 500; text-align: center; line-height: 10px;
    display: flex; flex-direction: column; align-items: center; padding-top: 22px; gap: 12px; }
  .service-card svg { width: 24px; height: 30px; }
  .progress { left: 410px; top: 774px; width: 135px; height: 1px; background: var(--line); }
  .progress-fill { left: 410px; top: 773px; width: 26px; height: 2px; background: var(--navy); }
  .arrow-btn { width: 18px; height: 18px; border-radius: 50%; border: 1px solid #9bb0cc; display: flex; align-items: center; justify-content: center; }

  /* CTA */
  .cta-band { left: 0; top: 811px; width: 716px; height: 99px; background: linear-gradient(100deg, #083d84 0%, #0a468f 60%, #083d84 100%); }
  .cta-text { left: 96px; top: 834px; width: 290px; font-size: 11.5px; line-height: 17.5px; font-weight: 700; color: var(--white); }

  /* Contact */
  .map-area { left: 96px; top: 950px; width: 269px; height: 179px;
    background: linear-gradient(135deg, #eef0f2 0%, #e6e9ec 55%, #aad3f2 75%, #a6cff0 100%); }
  .contact-item { left: 396px; display: flex; gap: 6px; font-size: 7.2px; line-height: 14px; color: var(--ink); }
  .contact-item svg { flex: none; width: 9px; height: 11px; margin-top: 1px; }

  /* Footer */
  .footer-brand { left: 96px; top: 1171px; font-size: 10px; font-weight: 600; letter-spacing: 1px; color: var(--navy-deep); }
  .footer-note { right: 96px; top: 1173px; font-size: 6.5px; color: var(--muted); }
</style>
</head>
<body>

  <header class="abs hero" role="img" aria-label="Construction planning scene with blueprints and glasses, tinted navy"></header>
  <nav class="abs site-nav">
    <div class="brand"><span class="brand-dot"></span>QELVORBIS</div>
    <div class="nav-links">
      <span>Home</span><span>About us</span><span>Services &#8964;</span><span>Contact us</span>
    </div>
  </nav>
  <h1 class="abs hero-title">We provides our clients with in-depth plan &amp; cost construction funding, environmental and property condition reports.</h1>
  <a class="abs btn btn-light" style="left:96px;top:227px;width:90px;height:22px;">Discover more</a>

  <div class="abs house-photo" role="img" aria-label="Photo of Victorian row houses against a city skyline"></div>
  <p class="abs eyebrow">ABOUT US</p>
  <h2 class="abs section-title" style="left:96px;top:381px;width:260px;">Decades of Experience in Every Phase of Construction</h2>
  <p class="abs copy" style="left:96px;top:431px;width:275px;">With over 25 years experience we provide customized and comprehensive inspection services to financial institutions involved in construction and loan management in New York, New Jersey, Pennsylvania and surrounding areas.</p>
  <a class="abs btn btn-dark" style="left:96px;top:511px;width:90px;height:22px;">Learn more</a>

  <div class="abs services-band" role="img" aria-label="Faint photo of building steel framework"></div>
  <h2 class="abs section-title" style="left:96px;top:608px;">Services</h2>
  <p class="abs copy" style="left:96px;top:627px;width:235px;">We are committed to providing our clients with expert analysis of proposed and ongoing construction projects –providing crucial facts that will lead to lending decisions that end in success.</p>
  <a class="abs btn btn-dark" style="left:96px;top:718px;width:90px;height:22px;">Learn more</a>

  <div class="abs service-card" style="left:365px;top:645px;">
    <svg viewBox="0 0 24 30" fill="none" stroke="#fff" stroke-width="1.3"><rect x="2" y="2" width="18" height="26" rx="1"/><path d="M6 8h10M6 12h10M6 16h6"/><circle cx="15" cy="21" r="3"/></svg>
    <span>Property Condition<br>Reports</span>
  </div>
  <div class="abs service-card" style="left:499px;top:645px;">
    <svg viewBox="0 0 24 30" fill="none" stroke="#fff" stroke-width="1.3"><rect x="2" y="3" width="9" height="11" rx="1"/><rect x="13" y="15" width="9" height="12" rx="1"/><path d="M11 8h5v7M13 21H7v-7"/></svg>
    <span>Plan &amp; Cost Reviews</span>
  </div>
  <div class="abs service-card" style="left:633px;top:645px;width:120px;">
    <svg viewBox="0 0 24 30" fill="none" stroke="#fff" stroke-width="1.3"><rect x="2" y="2" width="15" height="24" rx="1"/><path d="M5 8h9M5 12h6"/><circle cx="16" cy="19" r="4"/><path d="M19 22l4 4"/></svg>
    <span>Construction Funding<br>Inspections</span>
  </div>
  <div class="abs progress"></div>
  <div class="abs progress-fill"></div>
  <div class="abs arrow-btn" style="left:579px;top:766px;"><svg width="7" height="7" viewBox="0 0 7 7" fill="none" stroke="#083f86" stroke-width="1"><path d="M6.5 3.5H.8M3.3 1 .8 3.5 3.3 6"/></svg></div>
  <div class="abs arrow-btn" style="left:601px;top:766px;border-color:#083f86;"><svg width="7" height="7" viewBox="0 0 7 7" fill="none" stroke="#083f86" stroke-width="1"><path d="M.5 3.5h5.7M3.7 1l2.5 2.5L3.7 6"/></svg></div>

  <section class="abs cta-band"></section>
  <p class="abs cta-text">We will give you the essential facts that are critical for solid business decision making and ongoing loan management</p>
  <a class="abs btn btn-light" style="left:477px;top:847px;width:143px;height:27px;">Download Quote Request Form</a>

  <div class="abs map-area" role="img" aria-label="Street map showing the office location beside a lake"></div>
  <h2 class="abs section-title" style="left:396px;top:968px;">Contact us</h2>
  <div class="abs contact-item" style="top:1013px;">
    <svg viewBox="0 0 9 11" fill="none" stroke="#083f86" stroke-width="1"><path d="M4.5 10.5S1 6.6 1 4.3a3.5 3.5 0 0 1 7 0c0 2.3-3.5 6.2-3.5 6.2z"/><circle cx="4.5" cy="4.3" r="1.2"/></svg>
    <span>418 Linden Ridge Rd Suite 12 Marlow Township,<br>NJ 07940.</span>
  </div>
  <div class="abs contact-item" style="top:1055px;">
    <svg viewBox="0 0 9 11" fill="none" stroke="#083f86" stroke-width="1"><rect x="1.5" y=".5" width="6" height="10" rx="1"/><path d="M3.5 8.5h2"/></svg>
    <span>973-555-0147</span>
  </div>
  <div class="abs contact-item" style="top:1081px;">
    <svg viewBox="0 0 9 11" fill="none" stroke="#083f86" stroke-width="1"><rect x=".5" y="2.5" width="8" height="6" rx="1"/><path d="M.8 3l3.7 3 3.7-3"/></svg>
    <span>info@qelvorbis.com</span>
  </div>

  <footer>
    <div class="abs footer-brand">QELVORBIS CONSULTANTS</div>
    <div class="abs footer-note">© Copyright 2019 Qelvorbis Consultants. All rights reserved</div>
  </footer>

</body>
</html>
```